Login screen design for grocery app

Hi,

We are working on a grocery delivery app and need a design for its launch screen. This is the screen where the user clicks on either Login or Register. You can see our current login screen (and app name) in the attached image. You should use the same background color.

We are looking for designs that have to do with groceries (fruits/vegetables/diary products/chocolate etc).

Note: We do not want a login form on the launch screen, only a Login and Register button.

Let me know if you have any questions.

Regards.

Industry/Entity Type

Grocery Store

Colors
886aae
6b449b
e34298
ffffff
9bcb3c
f78f20
f04a50
33b8a4
34a6d7

Requirements
Must have
• The design must have to do with groceries.

```html
<!DOCTYPE html>
<html lang="en">
<head>
<meta charset="utf-8">
<title>fresco — Launch Screen</title>
<link rel="stylesheet" href="https://fonts.googleapis.com/css2?family=Quicksand:wght@400&family=Open+Sans:wght@400;600&display=swap">
<style>
  :root {
    --stage-bg: #eceff3;
    --screen-bg: #6a3bb5;
    --accent-pink: #e3429a;
    --white: #ffffff;
    --cart-grey: #e6e6ea;
    --art-green: #9bcb3c;
    --art-orange: #f78f20;
    --art-red: #f04a50;
    --art-teal: #33b8a4;
    --art-yellow: #f7d21e;
    --art-plum: #7a2a6e;
  }
  html, body {
    margin: 0;
    padding: 0;
    width: 1200px;
    height: 998px;
    overflow: hidden;
    background: var(--stage-bg);
  }
  .stage {
    position: relative;
    width: 1200px;
    height: 998px;
  }
  .launch-screen {
    position: absolute;
    left: 338px;
    top: 33px;
    width: 640px;
    height: 1136px;
    transform: scale(0.82);
    transform-origin: top left;
    background: var(--screen-bg);
    box-shadow: 0 4px 14px rgba(0, 0, 0, 0.35);
    color: var(--white);
    font-family: "Open Sans", sans-serif;
  }
  .status-bar {
    position: absolute;
    left: 0;
    top: 0;
    width: 640px;
    height: 44px;
  }
  .status-bar__signal {
    position: absolute;
    left: 12px;
    top: 15px;
  }
  .status-bar__time {
    position: absolute;
    left: 0;
    right: 0;
    top: 5px;
    text-align: center;
    font-weight: 600;
    font-size: 24px;
  }
  .status-bar__battery {
    position: absolute;
    right: 12px;
    top: 5px;
    display: flex;
    align-items: center;
    gap: 8px;
    font-size: 24px;
  }
  .brand-name {
    position: absolute;
    left: 0;
    right: 0;
    top: 160px;
    text-align: center;
    font-family: "Quicksand", sans-serif;
    font-weight: 400;
    font-size: 124px;
    letter-spacing: 4px;
    line-height: 1;
    margin: 0;
  }
  .hero-art {
    position: absolute;
    left: 115px;
    top: 380px;
    width: 372px;
    height: 322px;
    border-radius: 40% 40% 30% 30% / 30% 30% 20% 20%;
    background:
      radial-gradient(ellipse 30% 28% at 30% 38%, var(--art-orange), transparent 70%),
      radial-gradient(ellipse 26% 30% at 70% 30%, var(--art-orange), transparent 70%),
      radial-gradient(ellipse 24% 26% at 55% 42%, var(--art-yellow), transparent 70%),
      radial-gradient(ellipse 26% 26% at 82% 40%, var(--art-green), transparent 70%),
      radial-gradient(ellipse 22% 24% at 22% 30%, var(--art-teal), transparent 70%),
      radial-gradient(ellipse 24% 20% at 45% 52%, var(--art-red), transparent 70%),
      radial-gradient(ellipse 22% 18% at 30% 52%, var(--art-plum), transparent 70%),
      linear-gradient(180deg, rgba(255,255,255,0.15) 0%, rgba(230,230,234,0.55) 62%, rgba(230,230,234,0.85) 100%);
  }
  .btn {
    position: absolute;
    left: 130px;
    width: 380px;
    height: 80px;
    box-sizing: border-box;
    border-radius: 40px;
    display: flex;
    align-items: center;
    justify-content: center;
    font-weight: 400;
    font-size: 25px;
    letter-spacing: 2px;
    color: var(--white);
    box-shadow: 0 4px 8px rgba(40, 10, 80, 0.35);
  }
  .btn--login {
    top: 770px;
    background: var(--accent-pink);
  }
  .btn--register {
    top: 903px;
    border: 4px solid var(--white);
    background: transparent;
  }
</style>
</head>
<body>
<main class="stage">
  <section class="launch-screen">
    <div class="status-bar">
      <svg class="status-bar__signal" width="70" height="14" viewBox="0 0 70 14" aria-hidden="true">
        <circle cx="6" cy="7" r="5.5" fill="#fff"/>
        <circle cx="20" cy="7" r="5.5" fill="#fff"/>
        <circle cx="34" cy="7" r="5.5" fill="#fff"/>
        <circle cx="48" cy="7" r="5.5" fill="#fff"/>
        <circle cx="62" cy="7" r="5.5" fill="#fff"/>
      </svg>
      <div class="status-bar__time">10:30 PM</div>
      <div class="status-bar__battery">
        <span>100%</span>
        <svg width="48" height="20" viewBox="0 0 48 20" aria-hidden="true">
          <rect x="1" y="1" width="42" height="18" rx="2" fill="#fff" stroke="#fff" stroke-width="1.5"/>
          <rect x="44" y="6" width="3" height="8" rx="1" fill="#fff"/>
        </svg>
      </div>
    </div>

    <h1 class="brand-name">fresco</h1>

    <div class="hero-art" role="img" aria-label="Illustration of a speeding grocery shopping cart full of fresh food: a water bottle, peppers, bread, bananas, watermelon, tomatoes and eggplant, with motion lines behind it"></div>

    <div class="btn btn--login">LOGIN</div>
    <div class="btn btn--register">REGISTER</div>
  </section>
</main>
</body>
</html>
```